Corporate WordPress Site for Global IT Staffing Firm

We are looking for a corporate web presence for our company, Quillex, that is an IT Staffing and Recruiting firm based in Silicon Valley. We want the site to convey strength, confidence and trust in our F500 global customers and be appealing to prospective job seekers looking for their next employment.
I've attached the logo scheme to you. I can provide content within the next few days as well as links to our Chirply, PB pages. I also have wallpaper images selected from Marrow stills for a scrolling banner. Eventually we'll post job openings with search capabilities from a third party VMS SaaS company called Tidewick.
Target Market(s)
Global 1000 companies who purchase staffing from our firm AND prospective job seekers looking for work.
Industry/Entity Type
It Company
Number of Pages Required
3 page
Requirements
Must have
- Modern, parallax design for corporate image. May need links and integration to third party systems in a few months.
- Want each of the images via slider or images to convey:
- Attention to Detail
- Taking the Time to Find the Right Candidates
- Old Fashioned Hard Work
- Assembling the Right Teams
- Built to Scale
Nice to have
- Sliders. Counters. Links to social media pages. Background information. Bio pages. Reference customers.
- Examples of sites we like.
- https://www.rydexo.example/
- http://www.palvinmediaset.example/
- http://www.qornaworks.example/

```html
<!DOCTYPE html>
<html lang="en">
<head>
<meta charset="utf-8">
<title>Quillex — Contact</title>
<link rel="stylesheet" href="https://fonts.googleapis.com/css2?family=Lato:wght@300;400;700&display=swap">
<style>
  :root {
    --ink: #3d3d3d;
    --muted: #8a8a8a;
    --label: #2e2e2e;
    --line: #dcdcdc;
    --accent: #5876a6;
    --accent-dark: #3f5d8c;
    --divider: #a9b3d0;
    --hero-top: #6f7478;
    --hero-bottom: #b8babd;
    --map-a: #e6e6e6;
    --map-b: #d4d4d4;
    --pin: #8c8c8c;
    --footer-bg: #f4f4f4;
    --white: #ffffff;
  }
  * { box-sizing: border-box; margin: 0; padding: 0; }
  html, body { width: 772px; height: 1200px; overflow: hidden; }
  body { position: relative; background: var(--white); font-family: "Lato", sans-serif; color: var(--ink); }

  .hero {
    position: absolute; left: 0; top: 0; width: 772px; height: 242px;
    background: linear-gradient(180deg, var(--hero-top) 0%, #9b9ea2 45%, var(--hero-bottom) 100%);
  }
  .site-header {
    position: absolute; left: 0; top: 0; width: 772px; height: 49px;
    border-bottom: 1px solid rgba(255,255,255,0.35);
  }
  .brand {
    position: absolute; left: 29px; top: 15px; display: flex; align-items: center; gap: 6px;
    color: var(--white); font-weight: 700; font-size: 16px; letter-spacing: 0.2px;
  }
  .brand-dot { width: 11px; height: 11px; border-radius: 50%; background: var(--white); }
  .nav { position: absolute; top: 19px; left: 548px; }
  .nav a { color: var(--white); text-decoration: none; font-size: 8.5px; font-weight: 700; position: absolute; white-space: nowrap; }
  .nav .about { left: 0; }
  .nav .services { left: 40px; }
  .nav .contact { left: 86px; }
  .nav-active-bar { position: absolute; left: 644px; top: 0; width: 20px; height: 4px; background: var(--accent); }
  .search-jobs {
    position: absolute; left: 676px; top: 13px; width: 72px; height: 22px;
    border: 1px solid var(--white); border-radius: 11px; color: var(--white);
    font-size: 8px; font-weight: 700; display: flex; align-items: center; justify-content: center;
  }
  .page-title {
    position: absolute; left: 0; top: 190px; width: 772px; text-align: center;
    color: var(--white); font-size: 24px; font-weight: 400; letter-spacing: 0.5px;
  }

  .intro { position: absolute; left: 0; top: 296px; width: 772px; text-align: center; }
  .intro h2 { font-size: 13px; font-weight: 400; letter-spacing: 0.6px; color: var(--ink); }
  .intro .divider { width: 57px; height: 1px; background: var(--divider); margin: 14px auto 0; }
  .intro p { width: 400px; margin: 14px auto 0; font-size: 9.5px; line-height: 13px; color: var(--muted); }

  .contact-info { position: absolute; left: 59px; top: 423px; }
  .info-block { position: absolute; left: 0; white-space: nowrap; }
  .info-block h4 { font-size: 6.5px; font-weight: 700; color: var(--label); letter-spacing: 0.4px; }
  .info-block p { font-size: 8px; color: var(--muted); margin-top: 5px; }

  .field { position: absolute; }
  .field label { display: block; font-size: 6.5px; font-weight: 700; color: var(--label); letter-spacing: 0.3px; }
  .field .box { margin-top: 4px; border: 1px solid var(--line); background: var(--white); }
  .send-btn {
    position: absolute; left: 591px; top: 689px; width: 118px; height: 32px; border-radius: 16px;
    background: var(--accent); border: 1px solid var(--accent-dark); color: var(--white);
    font-size: 8.5px; font-weight: 700; letter-spacing: 0.8px;
    display: flex; align-items: center; justify-content: center;
  }

  .map {
    position: absolute; left: 0; top: 803px; width: 772px; height: 224px;
    background: linear-gradient(120deg, var(--map-a) 0%, var(--map-b) 55%, var(--map-a) 100%);
  }
  .map-pin { position: absolute; left: 430px; top: 923px; width: 18px; height: 26px; }

  .site-footer { position: absolute; left: 0; top: 1027px; width: 772px; height: 173px; background: var(--footer-bg); }
  .footer-col { position: absolute; top: 36px; }
  .footer-col h5 { font-size: 6px; font-weight: 700; color: var(--label); letter-spacing: 0.4px; height: 7px; }
  .footer-col ul { list-style: none; margin-top: 10px; }
  .footer-col li { font-size: 6px; color: var(--muted); line-height: 10.5px; white-space: nowrap; }
  .footer-brand { position: absolute; left: 577px; top: 33px; }
  .footer-brand .mark { width: 20px; height: 20px; border-radius: 50%; background: #9a9a9a; }
  .footer-brand p { font-size: 6px; color: var(--muted); line-height: 9.5px; width: 150px; margin-top: 8px; }
  .footer-rule { position: absolute; left: 48px; top: 117px; width: 677px; height: 1px; background: var(--line); }
  .copyright { position: absolute; left: 48px; top: 130px; font-size: 6px; color: var(--muted); }
  .social { position: absolute; right: 47px; top: 128px; display: flex; gap: 8px; font-size: 6px; color: var(--muted); }
</style>
</head>
<body>
  <section class="hero" role="img" aria-label="Photograph of people working at a desk with glasses, pens and paperwork">
    <header class="site-header">
      <div class="brand"><span class="brand-dot"></span>Quillex</div>
      <nav class="nav">
        <a class="about" href="#">About</a>
        <a class="services" href="#">Services</a>
        <a class="contact" href="#">Contact</a>
      </nav>
    </header>
    <span class="nav-active-bar"></span>
    <a class="search-jobs">Search Jobs</a>
    <h1 class="page-title">CONTACT</h1>
  </section>

  <section class="intro">
    <h2>A SAMPLE HEADLINE LOREM IPSUM</h2>
    <div class="divider"></div>
    <p>Lorem ipsum dolor sit amet, sed do eiusmod tempor incididunt ut labore et dolore magna. Quis nostrud exercitation ullamco laboris nisi ut aliquip ex ea commodo consequat.</p>
  </section>

  <aside class="contact-info">
    <div class="info-block" style="top:0"><h4>OFFICE ADDRESS</h4><p>48 Larkfield Row, Marlow Heights</p></div>
    <div class="info-block" style="top:42px"><h4>TELEFAX</h4><p>(+555) 014 2290 or +55 501 48836</p></div>
    <div class="info-block" style="top:76px"><h4>MOBILE</h4><p>(+555) 014 2290 or +55 501 48836</p></div>
    <div class="info-block" style="top:114px"><h4>EMAIL</h4><p>info@quillex.com</p></div>
  </aside>

  <form class="contact-form">
    <div class="field" style="left:247px; top:423px;"><label>YOUR NAME *</label><div class="box" style="width:222px;height:25px"></div></div>
    <div class="field" style="left:487px; top:423px;"><label>EMAIL ADDRESS *</label><div class="box" style="width:222px;height:25px"></div></div>
    <div class="field" style="left:247px; top:474px;"><label>CONTACT NUMBER *</label><div class="box" style="width:222px;height:25px"></div></div>
    <div class="field" style="left:487px; top:474px;"><label>MESSAGE TITLE</label><div class="box" style="width:222px;height:25px"></div></div>
    <div class="field" style="left:247px; top:531px;"><label>MESSAGE *</label><div class="box" style="width:462px;height:128px"></div></div>
    <div class="send-btn">SEND MESSAGE</div>
  </form>

  <div class="map" role="img" aria-label="Greyscale street map of the valley around the office, with towns, highways and a location pin"></div>
  <svg class="map-pin" viewBox="0 0 18 26" aria-hidden="true">
    <path d="M9 0C4 0 0 4 0 9c0 7 9 17 9 17s9-10 9-17C18 4 14 0 9 0z" fill="var(--pin)"/>
    <circle cx="9" cy="9" r="3.5" fill="var(--map-a)"/>
  </svg>

  <footer class="site-footer">
    <div class="footer-col" style="left:48px;">
      <h5>ABOUT QUILLEX</h5>
      <ul>
        <li>Sed ut perspiciatis unde omnis iste natus</li>
        <li>Error sit voluptatem accusantium doloreque</li>
        <li>Laudantium, totam rem aperiam</li>
      </ul>
    </div>
    <div class="footer-col" style="left:188px;">
      <h5></h5>
      <ul>
        <li>Sed ut perspiciatis unde omnis iste natus</li>
        <li>Error sit voluptatem accusantium doloreque</li>
        <li>Laudantium, totam rem aperiam</li>
      </ul>
    </div>
    <div class="footer-col" style="left:352px;">
      <h5>CONTACT US</h5>
      <ul>
        <li>(+555) 014 2290 or +55 501 48836</li>
        <li>info@quillex.com</li>
        <li>48 Larkfield Row, Marlow Heights</li>
      </ul>
    </div>
    <div class="footer-brand">
      <div class="mark"></div>
      <p>Quillex is a lorem ipsum dolor sit amet, consectetur adipi scing elit.</p>
    </div>
    <div class="footer-rule"></div>
    <p class="copyright">Copyright © 2015 Quillex. &nbsp;Terms &amp; Conditions &nbsp;|&nbsp; Sitemap &nbsp;|&nbsp; Contact</p>
    <div class="social"><span>PB</span><span>Chirply</span><span>Pictora</span></div>
  </footer>
</body>
</html>
```